Home page web design for "Tales from Thee"

We need a home page web design for a start up company that will write memoirs for seniors.
The completed project will need to include PSD files...NO HTML or CSS necessary.
Attached is a brief outline concept that may give you some ideas...but you are the creative professionals, so please feel free to add your ideas. We will also attach some files that show you our logo, brochures, and photos that could be used to give you ideas of our focus.
There will need to be access to the other pages on the home page to include: 'About Us'; 'How We Can Help'; 'Community Sessions'; 'Senior Consulting ' and 'Contact Us'.
Updates

Target Market(s)

Seniors and Baby Boomers

Industry/Entity Type

It Company

Number of Pages Required

1 page

Colors
f9ba93
fbca95
faa54b
faf289
f37123

Requirements
Must have
• Script easy on senior eyes.
• Initial contact number would be 844-4LANTERN
Nice to have
• While the color pallet is non-specific we prefer the warm colors.
• salmon, peach.......
• NOT so much the orange of Halloween:)
• However, please utilize your creativity and put in colors you feel will draw best with your design.

```html
<!DOCTYPE html>
<html lang="en">
<head>
<meta charset="utf-8">
<title>Tales from Thee — Home</title>
<link rel="stylesheet" href="https://fonts.googleapis.com/css2?family=Open+Sans:ital,wght@0,400;0,600;0,700;1,400;1,600&family=Tangerine:wght@700&display=swap">
<style>
:root{
  --gold:#c9a85a;
  --gold-dark:#8a6a2c;
  --brown:#7b5c26;
  --brown-deep:#5e4419;
  --field:#5a4118;
  --title:#6e5224;
  --text:#5a5a5a;
  --text-dark:#3f3f3f;
  --header:#efefef;
  --paper:#e8e8e6;
  --white:#ffffff;
  --orange:#f7a21b;
  --orange-deep:#f37123;
}
*{margin:0;padding:0;box-sizing:border-box}
html,body{width:1200px;height:2296px;overflow:hidden}
body{position:relative;font-family:"Open Sans",Arial,sans-serif;color:var(--text);background:var(--header)}
.abs{position:absolute}
.script{font-family:"Tangerine",cursive;font-weight:700;color:var(--title)}

/* header */
.site-header{left:0;top:0;width:1200px;height:95px;background:var(--header)}
.phone{left:100px;top:17px;display:flex;align-items:center;gap:12px;font-size:19px;font-weight:600;color:var(--gold-dark)}
.phone-badge{width:28px;height:28px;border-radius:50%;background:var(--gold);display:flex;align-items:center;justify-content:center}
.nav{top:63px;display:flex;gap:26px;font-size:13px;color:#555;text-transform:uppercase}
.nav-left{left:98px}
.nav-right{left:764px}
.socials{left:925px;top:17px;display:flex;gap:9px}
.socials span{width:28px;height:28px;border-radius:50%;background:var(--gold)}
.socials span:first-child{background:var(--gold-dark)}
.logo-disc{left:418px;top:-120px;width:302px;height:265px;border-radius:50%;background:#f7f7f7;display:flex;align-items:flex-end;justify-content:center;padding-bottom:52px}
.logo-name{font-family:"Tangerine",cursive;font-weight:700;font-size:50px;color:var(--gold-dark)}

/* hero */
.hero{left:0;top:95px;width:1200px;height:441px;background:linear-gradient(90deg,#2d2a22 0%,#3b3527 40%,#4b4433 62%,#2a2620 100%)}
.hero-portrait{left:560px;top:95px;width:560px;height:441px;background:radial-gradient(ellipse at 45% 40%,#8a7260 0%,#5a4a3c 40%,rgba(45,40,32,0) 75%)}
.hero-title{left:101px;top:220px;font-family:"Tangerine",cursive;font-weight:700;font-size:62px;line-height:56px;color:#f1dfb0}
.btn-more{left:101px;top:393px;width:125px;height:37px;border:1px solid #e9dcc0;color:#f4ecd9;font-size:15px;display:flex;align-items:center;justify-content:center}

/* about */
.about{left:0;top:536px;width:1200px;height:838px;background:var(--paper)}
.avatar{border-radius:50%;border:5px solid #fff;box-shadow:0 1px 4px rgba(0,0,0,.25)}
.about-avatar{left:144px;top:569px;width:184px;height:184px;background:radial-gradient(circle at 50% 38%,#a08878 0%,#5d4c40 55%,#3d342c 100%)}
.section-title{font-size:42px;line-height:1}
.rule{height:16px}
.about-title{left:347px;top:568px}
.about-rule{left:347px;top:618px;width:300px}
.about-lead{left:346px;top:656px;width:720px;font-size:15px;line-height:23px;color:var(--text-dark)}
.about-lead h3{font-size:17px;font-weight:600;color:var(--brown-deep);margin-bottom:3px}
.about-body{left:144px;top:776px;width:912px;font-size:14.5px;line-height:19px;color:var(--text-dark)}
.about-body p{margin-bottom:10px}
.books-title{left:0;top:1030px;width:1200px;text-align:center}
.books-rule{left:340px;top:1082px;width:520px}
.book{top:1118px;width:142px;height:195px;box-shadow:2px 3px 6px rgba(0,0,0,.3)}
.shelf{left:144px;top:1304px;width:912px;height:22px;background:linear-gradient(#f5dcae,#d8b177);box-shadow:0 4px 5px rgba(0,0,0,.2)}
.bracket{top:1326px;width:9px;height:18px;background:#cfcfcf;border:1px solid #999}

/* blog */
.blog{left:0;top:1374px;width:1200px;height:320px;background:var(--white)}
.blog-title{left:145px;top:1394px}
.blog-rule{left:145px;top:1443px;width:320px}
.post-date{top:1482px;width:52px;height:52px;background:var(--brown);color:#fff;font-size:11px;font-weight:700;line-height:13px;text-align:center;padding-top:6px}
.post-meta{top:1604px;width:52px;font-size:10px;text-align:center;color:#666}
.post-img{top:1482px;width:231px;height:141px}
.post-text{top:1630px;width:231px;font-size:12px;line-height:17px;color:var(--text-dark)}
.icon-comment{top:1548px}
.icon-like{top:1584px}

/* testimonials */
.clients{left:0;top:1694px;width:1200px;height:314px;background:var(--header)}
.clients-title{left:145px;top:1728px}
.clients-rule{left:145px;top:1777px;width:320px}
.client-avatar{left:148px;top:1814px;width:114px;height:114px;background:radial-gradient(circle at 50% 40%,#8b6a58 0%,#3a2b25 65%,#1e1815 100%)}
.client-name{left:120px;top:1948px;width:170px;text-align:center;font-size:14px;line-height:19px}
.client-name b{color:var(--brown);font-weight:600}
.quote{left:314px;top:1822px;width:745px;font-size:14px;line-height:31px;font-style:italic;font-weight:600;color:#6a6a6a}
.dots{left:955px;top:1967px;display:flex;gap:8px}
.dots span{width:15px;height:15px;border-radius:50%;background:#c7c7c7}
.dots span:first-child{background:var(--brown)}

/* contact */
.contact{left:0;top:2008px;width:1200px;height:233px;background:var(--brown)}
.contact-heading{font-size:17px;font-weight:700;color:#fff;text-transform:uppercase}
.field{background:var(--field);border-radius:6px;color:#c4b08a;font-size:13px;padding:11px 17px}
.submit{left:646px;top:2121px;width:99px;height:92px;border-radius:6px;background:linear-gradient(135deg,#ffc23a,var(--orange-deep));color:#2a1c05;font-weight:700;font-size:15px;display:flex;align-items:center;justify-content:center}
.visit-row{position:absolute;left:813px;display:flex;gap:12px;color:#fff;font-size:13.5px;line-height:19px}
.visit-row svg{flex:none}

/* bottom bar */
.bottom{left:0;top:2241px;width:1200px;height:55px;background:var(--header)}
.bottom-text{top:2259px;font-size:12px;color:#666}
.bottom-links{left:152px}
.bottom-copy{left:755px}
.bottom-copy b{color:var(--brown);font-weight:600}
</style>
</head>
<body>

<header class="abs site-header"></header>
<div class="abs phone"><span class="phone-badge"><svg width="14" height="14" viewBox="0 0 24 24"><path fill="#fff" d="M6.6 10.8c1.4 2.8 3.8 5.1 6.6 6.6l2.2-2.2c.3-.3.7-.4 1-.2 1.1.4 2.3.6 3.6.6.6 0 1 .4 1 1V20c0 .6-.4 1-1 1C10.6 21 3 13.4 3 4c0-.6.4-1 1-1h3.5c.6 0 1 .4 1 1 0 1.3.2 2.5.6 3.6.1.3 0 .7-.2 1z"/></svg></span>844-4LANTERN</div>
<nav class="abs nav nav-left"><span>Home</span><span>About Us</span><span>How We Can Help</span></nav>
<nav class="abs nav nav-right"><span>Community</span><span>Senior Consulting</span><span>Contact Us</span></nav>
<div class="abs socials" aria-label="Social links"><span></span><span></span><span></span><span></span><span></span></div>
<div class="abs logo-disc"><span class="logo-name">Tales from Thee</span></div>

<section class="abs hero" role="img" aria-label="Photo of an elderly man holding up his printed memoir book"></section>
<div class="abs hero-portrait"></div>
<h1 class="abs hero-title">Ordinary Lives………<br>Extraordinary Legacies</h1>
<div class="abs btn-more">Read More</div>

<section class="abs about"></section>
<div class="abs avatar about-avatar" role="img" aria-label="Portrait of an elderly man with his memoir"></div>
<h2 class="abs section-title script about-title">Shortly about me</h2>
<svg class="abs rule about-rule" viewBox="0 0 300 16"><circle cx="14" cy="8" r="4" fill="var(--gold-dark)"/><line x1="26" y1="8" x2="300" y2="8" stroke="var(--gold-dark)"/></svg>
<div class="abs about-lead">
  <h3>When a genealogy doesn’t say enough!</h3>
  If you were alive in 100 years, what would you share with your descendants?<br>
  Now you have a vehicle to help you immortalize your thoughts for the future…specifically for those who will want to know!
</div>
<div class="abs about-body">
  <p>We are not all presidents of countries or CEO’s of fortune 500 companies! But “every life legacy is a gift to be treasured by the next generation.”</p>
  <p>Does your family host generations of soldiers, doctors, farmers, scientists, mechanics, entrepreneurs, writers, politicians, contractors, pastors, artisans, athletes, musicians, etc..? Generational patterns can often emerge when writing your story that will interest the next generation.</p>
  <p>A genealogy, while very relevant, doesn’t offer the personal story of the names we find. A biography can place a deeper relevance on the face for future descendants. Every life is a legacy to pass forward and we at Tales from Thee believe everyone should chronicle their life journey in writing. This commitment allows you to be remembered for who you truly are as a person.</p>
  <p>Think about it….Do you know the triumphs and tribulations of your ancestors? Do you wish you did? Well, so will those falling into your personal family tree.</p>
</div>
<h2 class="abs section-title script books-title">Latest Books</h2>
<svg class="abs rule books-rule" viewBox="0 0 520 16"><line x1="0" y1="8" x2="240" y2="8" stroke="var(--gold-dark)"/><circle cx="260" cy="8" r="5" fill="var(--gold-dark)"/><line x1="280" y1="8" x2="520" y2="8" stroke="var(--gold-dark)"/></svg>
<div class="abs book" style="left:236px;background:linear-gradient(160deg,#f3c98a,#f0a856 60%,#fbe2b6)" role="img" aria-label="Book cover with family photos"></div>
<div class="abs book" style="left:430px;background:linear-gradient(170deg,#f6b860,#d98b3a 55%,#fbe7c4)" role="img" aria-label="Book cover with a senior writing"></div>
<div class="abs book" style="left:624px;background:linear-gradient(180deg,#c9d6e4 0%,#7e8aa0 45%,#f1a54f 78%,#fff 100%)" role="img" aria-label="Book cover with grandfather and baby"></div>
<div class="abs book" style="left:819px;background:linear-gradient(180deg,#b88a5e,#7a5a3c 55%,#f3b561 75%,#fff 100%)" role="img" aria-label="Book cover with a senior couple"></div>
<div class="abs shelf"></div>
<div class="abs bracket" style="left:262px"></div>
<div class="abs bracket" style="left:925px"></div>

<section class="abs blog"></section>
<h2 class="abs section-title script blog-title">Latest Blog</h2>
<svg class="abs rule blog-rule" viewBox="0 0 320 16"><circle cx="14" cy="8" r="4" fill="var(--gold-dark)"/><line x1="26" y1="8" x2="320" y2="8" stroke="var(--gold-dark)"/></svg>

<div class="abs post-date" style="left:144px">03<br>OCT<br>2014</div>
<div class="abs post-img" style="left:196px;background:linear-gradient(135deg,#8aa2bb,#3e4c5c)" role="img" aria-label="Photo of a smiling woman"></div>
<div class="abs post-text" style="left:196px">Lorem ipsum dolor sit amet consectetur adipiscing elit. Cras nec felis ut orci.</div>

<div class="abs post-date" style="left:459px">03<br>OCT<br>2014</div>
<div class="abs post-img" style="left:511px;background:linear-gradient(135deg,#5a4032,#c9b3a5 60%,#3a2a22)" role="img" aria-label="Photo of clasped hands"></div>
<div class="abs post-text" style="left:511px">Lorem ipsum dolor sit amet consectetur adipiscing elit. Cras nec felis ut orci.</div>

<div class="abs post-date" style="left:773px">03<br>OCT<br>2014</div>
<div class="abs post-img" style="left:825px;background:linear-gradient(135deg,#9fb8c4,#e6eef2 60%,#b7c9d1)" role="img" aria-label="Photo of a smiling woman in glasses"></div>
<div class="abs post-text" style="left:825px">Lorem ipsum dolor sit amet consectetur adipiscing elit. Cras nec felis ut orci.</div>

<svg class="abs icon-comment" style="left:158px" width="24" height="22" viewBox="0 0 24 22"><rect x="1" y="1" width="22" height="15" rx="2" fill="none" stroke="#777" stroke-width="1.5"/><path d="M6 16v5l5-5" fill="none" stroke="#777" stroke-width="1.5"/><path d="M12 5v7M8.5 8.5h7" stroke="#777" stroke-width="1.5"/></svg>
<svg class="abs icon-comment" style="left:473px" width="24" height="22" viewBox="0 0 24 22"><rect x="1" y="1" width="22" height="15" rx="2" fill="none" stroke="#777" stroke-width="1.5"/><path d="M6 16v5l5-5" fill="none" stroke="#777" stroke-width="1.5"/><path d="M12 5v7M8.5 8.5h7" stroke="#777" stroke-width="1.5"/></svg>
<svg class="abs icon-comment" style="left:787px" width="24" height="22" viewBox="0 0 24 22"><rect x="1" y="1" width="22" height="15" rx="2" fill="none" stroke="#777" stroke-width="1.5"/><path d="M6 16v5l5-5" fill="none" stroke="#777" stroke-width="1.5"/><path d="M12 5v7M8.5 8.5h7" stroke="#777" stroke-width="1.5"/></svg>
<svg class="abs icon-like" style="left:159px" width="22" height="19" viewBox="0 0 22 19"><path d="M11 18S1 11.5 1 6a5 5 0 0 1 10-1 5 5 0 0 1 10 1c0 5.5-10 12-10 12z" fill="none" stroke="#777" stroke-width="1.5"/></svg>
<svg class="abs icon-like" style="left:474px" width="22" height="19" viewBox="0 0 22 19"><path d="M11 18S1 11.5 1 6a5 5 0 0 1 10-1 5 5 0 0 1 10 1c0 5.5-10 12-10 12z" fill="none" stroke="#777" stroke-width="1.5"/></svg>
<svg class="abs icon-like" style="left:788px" width="22" height="19" viewBox="0 0 22 19"><path d="M11 18S1 11.5 1 6a5 5 0 0 1 10-1 5 5 0 0 1 10 1c0 5.5-10 12-10 12z" fill="none" stroke="#777" stroke-width="1.5"/></svg>
<div class="abs post-meta" style="left:144px">20</div>
<div class="abs post-meta" style="left:459px">20</div>
<div class="abs post-meta" style="left:773px">20</div>

<section class="abs clients"></section>
<h2 class="abs section-title script clients-title">What Our Happy Clients Say</h2>
<svg class="abs rule clients-rule" viewBox="0 0 320 16"><circle cx="14" cy="8" r="4" fill="var(--gold-dark)"/><line x1="26" y1="8" x2="320" y2="8" stroke="var(--gold-dark)"/></svg>
<div class="abs avatar client-avatar" role="img" aria-label="Client portrait"></div>
<div class="abs client-name"><b>Client Name</b><br>Position</div>
<p class="abs quote">Lorem ipsum dolor sit amet, consectetur adipiscing elit. Donec dolor metus, blandit vitae felis vitae, bibendum dignissim mauris. Maecenas quis quam ante. Aenean pretium efficitur lectus et malesuada. Nullam nec tellus libero. Nam convallis, lectus vel viverra blandit, lectus odio pretium sem, vitae varius nulla nulla …….</p>
<div class="abs dots"><span></span><span></span><span></span><span></span></div>

<section class="abs contact"></section>
<h4 class="abs contact-heading" style="left:144px;top:2027px">Contact Us</h4>
<div class="abs field" style="left:144px;top:2069px;width:294px;height:39px">Your Name:</div>
<div class="abs field" style="left:451px;top:2069px;width:294px;height:39px">Email:</div>
<div class="abs field" style="left:144px;top:2121px;width:488px;height:92px">Comments:</div>
<div class="abs submit">SUBMIT</div>
<h4 class="abs contact-heading" style="left:813px;top:2027px">Visit to Tales from Thee</h4>
<div class="visit-row" style="top:2064px"><svg width="26" height="30" viewBox="0 0 26 30"><path d="M12 2v27" stroke="#fff" stroke-width="2.5"/><path d="M3 6h19l3 3-3 3H3zM23 15H6l-3 3 3 3h17z" fill="#fff"/></svg><span>PO Box: 4720, lorem ipsum,<br>dolor, Australia 123456</span></div>
<div class="visit-row" style="top:2129px"><svg width="26" height="26" viewBox="0 0 24 24"><path fill="#fff" d="M6.6 10.8c1.4 2.8 3.8 5.1 6.6 6.6l2.2-2.2c.3-.3.7-.4 1-.2 1.1.4 2.3.6 3.6.6.6 0 1 .4 1 1V20c0 .6-.4 1-1 1C10.6 21 3 13.4 3 4c0-.6.4-1 1-1h3.5c.6 0 1 .4 1 1 0 1.3.2 2.5.6 3.6.1.3 0 .7-.2 1z"/></svg><span style="padding-top:2px">555-014-2270 &nbsp;/&nbsp; 844-4LANTERN</span></div>
<div class="visit-row" style="top:2191px"><svg width="26" height="20" viewBox="0 0 26 20"><rect x="1" y="2" width="24" height="16" fill="#fff"/><path d="M1 2l12 9 12-9" fill="none" stroke="var(--brown)" stroke-width="1.8"/></svg><span>hello@talesfromthee.com</span></div>

<footer class="abs bottom"></footer>
<div class="abs bottom-text bottom-links">Home &nbsp;/&nbsp; About Us &nbsp;/&nbsp; How We Can Help &nbsp;/&nbsp; Community &nbsp;/&nbsp; Senior Consulting &nbsp;/&nbsp; Contact Us</div>
<div class="abs bottom-text bottom-copy">© 2014 <b>Tales from Thee.</b> &nbsp;Privacy Policy &nbsp;|&nbsp; Terms of Use</div>

</body>
</html>
```